Financial Planning firm focused on serving women 55-65 yrs old needs stationary design

We are rebranding our financial planning firm and our target client is a 55-65 yr old women. We need a stationary design to go with our new logo.

Contact Information: Raymond Kessler, MBA Principal Harlow Wealth Management 4820 Bramblewood Lane, Suite 317 Alder Hollow, NV 89999 ray@harlowwealthmgmt.example phone 555-010-0184

```html
<!DOCTYPE html>
<html lang="en">
<head>
<meta charset="utf-8">
<title>Harlow Wealth Management — Stationery Set</title>
<link rel="stylesheet" href="https://fonts.googleapis.com/css2?family=Didact+Gothic&display=swap">
<style>
  :root {
    --blue: #2c6189;
    --sage: #9cb3a0;
    --green-text: #2f6b4a;
    --ink: #3a3a3a;
    --paper: #ffffff;
    --backdrop: #ecebe7;
    --edge: #c9c9c4;
    --font: "Didact Gothic", "Century Gothic", sans-serif;
  }
  * { box-sizing: border-box; margin: 0; padding: 0; }
  html, body { width: 1200px; height: 695px; overflow: hidden; }
  body { background: var(--backdrop); font-family: var(--font); color: var(--ink); position: relative; }

  .piece { position: absolute; background: var(--paper); border: 1px solid var(--edge); overflow: hidden; }
  .wave { position: absolute; left: 0; bottom: 0; width: 100%; display: block; }

  /* brand lockup */
  .brand { display: flex; flex-direction: column; align-items: center; color: var(--blue); }
  .brand-mark { border-radius: 50%; background: var(--sage); }
  .brand-name { font-size: 24px; letter-spacing: 2px; line-height: 1; margin-top: 6px; }
  .brand-sub { font-size: 5.5px; letter-spacing: 1px; text-transform: uppercase; margin-top: 2px; border-bottom: 1px solid var(--blue); padding-bottom: 1px; }

  /* letterhead */
  .letterhead { left: 23px; top: 31px; width: 498px; height: 644px; }
  .letterhead .brand { position: absolute; top: 10px; left: 0; width: 100%; }
  .letterhead .brand-mark { width: 46px; height: 46px; }
  .letterhead .wave { height: 100px; }
  .letterhead-contact { position: absolute; right: 16px; bottom: 8px; text-align: right; color: var(--paper); font-size: 9.5px; line-height: 1.55; }
  .letterhead-contact .address { font-size: 10px; margin-top: 4px; }
  .icon { display: inline-block; width: 8px; height: 8px; vertical-align: -1px; margin-right: 3px; }

  /* envelopes */
  .envelope-back { left: 616px; top: 38px; width: 517px; height: 242px; }
  .envelope-back .flap { position: absolute; left: 0; top: 0; width: 100%; height: 74px; background: var(--sage); }
  .envelope-back .flap-mark { position: absolute; left: 241px; top: 18px; width: 36px; height: 36px; border-radius: 50%; background: var(--paper); }

  .envelope-open { left: 578px; top: 148px; width: 555px; height: 242px; }
  .envelope-open svg { position: absolute; left: 0; top: 0; }
  .envelope-open .flap-mark { position: absolute; left: 255px; top: 14px; width: 42px; height: 42px; border-radius: 50%; background: var(--sage); }

  .envelope-front { left: 537px; top: 254px; width: 557px; height: 242px; }
  .envelope-front .brand { position: absolute; left: 12px; top: 6px; align-items: flex-start; }
  .envelope-front .brand-mark { width: 44px; height: 44px; margin-left: 10px; }
  .envelope-front .brand-name { font-size: 20px; }
  .envelope-front .return-address { position: absolute; left: 12px; top: 90px; font-size: 7.5px; line-height: 1.35; color: var(--ink); }
  .envelope-front .wave { height: 90px; }
  .envelope-front .site { position: absolute; right: 14px; bottom: 10px; color: var(--paper); font-size: 10px; letter-spacing: 0.5px; }

  /* business card */
  .card-front { left: 573px; top: 512px; width: 273px; height: 157px; }
  .card-front .brand { position: absolute; left: 16px; top: 8px; }
  .card-front .brand-mark { width: 44px; height: 44px; }
  .card-front .brand-name { font-size: 20px; }
  .card-front .holder { position: absolute; right: 10px; top: 10px; text-align: right; font-size: 8.5px; color: var(--blue); line-height: 1.2; }
  .card-front .holder small { font-size: 5.5px; }
  .card-front .holder .title { color: var(--green-text); font-size: 7px; }
  .card-front .wave { top: 64px; bottom: auto; height: 40px; }
  .card-front .card-contact { position: absolute; right: 10px; top: 92px; text-align: right; font-size: 6.5px; line-height: 1.3; color: var(--ink); }
  .card-front .card-contact .gap { margin-top: 5px; }
  .card-front .icon { width: 6px; height: 6px; }

  .card-back { left: 852px; top: 512px; width: 275px; height: 157px; background: var(--sage); border-color: var(--sage); }
  .card-back .back-mark { position: absolute; left: 112px; top: 26px; width: 52px; height: 52px; border-radius: 50%; background: var(--paper); }
  .card-back .site { position: absolute; left: 0; width: 100%; bottom: 18px; text-align: center; color: var(--paper); font-size: 8.5px; letter-spacing: 0.5px; }
</style>
</head>
<body>

<!-- Letterhead -->
<section class="piece letterhead">
  <div class="brand">
    <span class="brand-mark"></span>
    <span class="brand-name">HARLOW</span>
    <span class="brand-sub">Wealth Management</span>
  </div>
  <svg class="wave" viewBox="0 0 498 100" preserveAspectRatio="none" aria-hidden="true">
    <path d="M0 46 C150 70 330 8 498 6 L498 18 C330 20 160 76 0 58 Z" fill="var(--sage)"/>
    <path d="M0 66 C170 84 330 26 498 24 L498 100 L0 100 Z" fill="var(--blue)"/>
    <path d="M20 64 C180 80 330 26 498 20" stroke="var(--paper)" stroke-width="0.8" fill="none"/>
  </svg>
  <div class="letterhead-contact">
    <div><svg class="icon" viewBox="0 0 10 10"><circle cx="5" cy="5" r="5" fill="var(--paper)"/><path d="M3 2.5 L4 2.5 L4.6 4 L4 4.6 C4.4 5.4 4.8 5.8 5.5 6.1 L6 5.5 L7.5 6.1 L7.5 7.2 C5 7.4 2.8 5 3 2.5Z" fill="var(--blue)"/></svg>555-010-0184</div>
    <div><svg class="icon" viewBox="0 0 10 10"><rect x="0.5" y="2" width="9" height="6.5" fill="var(--paper)"/><path d="M0.5 2 L5 5.5 L9.5 2" stroke="var(--blue)" stroke-width="0.8" fill="none"/></svg>ray@harlowwealthmgmt.example</div>
    <div class="address">4820 Bramblewood Lane, Suite 317, Alder Hollow, NV 89999</div>
  </div>
</section>

<!-- Envelope back, flap closed -->
<section class="piece envelope-back">
  <div class="flap"><span class="flap-mark"></span></div>
</section>

<!-- Envelope back, flap open -->
<section class="piece envelope-open">
  <svg width="555" height="242" viewBox="0 0 555 242" aria-hidden="true">
    <path d="M0 0 L14 72 L541 72 L555 0" stroke="var(--ink)" stroke-width="0.8" fill="none"/>
  </svg>
  <span class="flap-mark"></span>
</section>

<!-- Envelope front -->
<section class="piece envelope-front">
  <div class="brand">
    <span class="brand-mark"></span>
    <span class="brand-name">HARLOW</span>
    <span class="brand-sub">Wealth Management</span>
  </div>
  <p class="return-address">4820 Bramblewood Lane<br>Suite 317, Alder Hollow, NV 89999</p>
  <svg class="wave" viewBox="0 0 557 90" preserveAspectRatio="none" aria-hidden="true">
    <path d="M0 30 C170 56 380 2 557 4 L557 12 C380 12 180 66 0 44 Z" fill="var(--sage)"/>
    <path d="M0 48 C190 70 380 18 557 14 L557 90 L0 90 Z" fill="var(--blue)"/>
    <path d="M30 50 C200 66 380 18 557 10" stroke="var(--paper)" stroke-width="0.7" fill="none"/>
  </svg>
  <span class="site">www.harlowwealthmgmt.example</span>
</section>

<!-- Business card front -->
<section class="piece card-front">
  <div class="brand">
    <span class="brand-mark"></span>
    <span class="brand-name">HARLOW</span>
    <span class="brand-sub">Wealth Management</span>
  </div>
  <div class="holder">
    Raymond Kessler, <small>MBA</small><br>
    <span class="title">Principal</span>
  </div>
  <svg class="wave" viewBox="0 0 273 40" preserveAspectRatio="none" aria-hidden="true">
    <path d="M0 26 C80 40 190 4 273 2 L273 8 C190 8 90 44 0 34 Z" fill="var(--sage)"/>
    <path d="M0 36 C90 44 190 12 273 10 L273 16 C190 18 90 46 0 42 Z" fill="var(--blue)"/>
  </svg>
  <div class="card-contact">
    <div>4820 Bramblewood Lane</div>
    <div>Suite 317, Alder Hollow, NV 89999</div>
    <div class="gap"><svg class="icon" viewBox="0 0 10 10"><circle cx="5" cy="5" r="5" fill="var(--ink)"/><path d="M3 2.5 L4 2.5 L4.6 4 L4 4.6 C4.4 5.4 4.8 5.8 5.5 6.1 L6 5.5 L7.5 6.1 L7.5 7.2 C5 7.4 2.8 5 3 2.5Z" fill="var(--paper)"/></svg>555-010-0184</div>
    <div><svg class="icon" viewBox="0 0 10 10"><rect x="0.5" y="2" width="9" height="6.5" fill="var(--ink)"/><path d="M0.5 2 L5 5.5 L9.5 2" stroke="var(--paper)" stroke-width="0.8" fill="none"/></svg>ray@harlowwealthmgmt.example</div>
  </div>
</section>

<!-- Business card back -->
<section class="piece card-back">
  <span class="back-mark"></span>
  <span class="site">www.harlowwealthmgmt.example</span>
</section>

</body>
</html>
```